BrindleCrewing Business Card Design

We are a staffing company finding positions for dedicated nurses and physicians.

Target Market(s)

Business Professionals

Industry/Entity Type

Staffing

Contact Information for Business Card

Gerald Pinkney
Chairman
417 39th Lantern West
ALDERMOOR BAY QX 00417
555-472-6158 Mobile
813-690-4137 Fax
gpinkney@brindlecrewing.com
www.brindlecrewing.com

Font styles to use
Sans Serif

Colors
fbee3e
f04a50
f37122

Requirements
Must have
• Logo Attached, see colors below. We'd like to see Yellow, Orange and Red.

```html
<!DOCTYPE html>
<html lang="en">
<head>
<meta charset="utf-8">
<title>BrindleCrewing Business Card</title>
<link rel="stylesheet" href="https://fonts.googleapis.com/css2?family=Lato:wght@400;700;900&display=swap">
<style>
  :root {
    --bg: #d9dce0;
    --card: #050505;
    --yellow: #fbee3e;
    --red: #f04a50;
    --orange: #f37122;
    --stripe-orange: #f7941d;
  }
  * { box-sizing: border-box; margin: 0; padding: 0; }
  html, body { width: 1200px; height: 900px; overflow: hidden; }
  body {
    background: var(--bg);
    font-family: "Lato", Arial, sans-serif;
    position: relative;
  }
  .card {
    position: absolute;
    left: 268px;
    width: 664px;
    height: 380px;
    background: var(--card);
    border-radius: 30px;
    overflow: hidden;
    box-shadow: 0 10px 26px rgba(0,0,0,0.25);
  }
  .card-back { top: 40px; }
  .card-front { top: 480px; }

  .brand {
    display: flex;
    align-items: center;
    gap: 14px;
  }
  .brand-name {
    font-weight: 900;
    color: var(--yellow);
    letter-spacing: -1px;
    line-height: 1;
  }
  .brand-dot {
    width: 22px;
    height: 22px;
    border-radius: 50%;
    background: var(--orange);
    flex: none;
  }

  /* back */
  .card-back .brand {
    position: absolute;
    left: 90px;
    top: 130px;
  }
  .card-back .brand-name { font-size: 72px; }
  .back-url {
    position: absolute;
    left: 140px;
    bottom: 72px;
    color: var(--stripe-orange);
    font-size: 15px;
  }
  .back-band {
    position: absolute;
    left: 0;
    right: 0;
    bottom: 34px;
    height: 30px;
    background: var(--stripe-orange);
  }

  /* front */
  .side-stripe {
    position: absolute;
    left: 0;
    top: 0;
    bottom: 0;
    width: 44px;
    display: flex;
    flex-direction: column;
  }
  .side-stripe span { display: block; }
  .side-stripe .seg-orange { background: var(--stripe-orange); flex: 0 0 30%; }
  .side-stripe .seg-red { background: var(--red); flex: 0 0 37%; }
  .side-stripe .seg-yellow { background: var(--yellow); flex: 1; }

  .card-front .brand {
    position: absolute;
    left: 82px;
    top: 50px;
  }
  .card-front .brand-name { font-size: 64px; }

  .person {
    position: absolute;
    left: 82px;
    top: 170px;
    width: 250px;
  }
  .person-name {
    color: var(--red);
    font-size: 28px;
    font-weight: 400;
    line-height: 1.1;
  }
  .person-title {
    color: var(--red);
    font-size: 20px;
    margin-top: 2px;
  }
  .person-address {
    color: var(--yellow);
    font-size: 14px;
    line-height: 1.35;
    margin-top: 12px;
  }

  .contacts {
    position: absolute;
    left: 350px;
    top: 186px;
    list-style: none;
  }
  .contacts li {
    display: flex;
    align-items: center;
    gap: 12px;
    color: var(--yellow);
    font-size: 17px;
    margin-bottom: 14px;
  }
  .contacts svg { width: 24px; height: 24px; flex: none; }
</style>
</head>
<body>

  <section class="card card-back" aria-label="Business card back">
    <div class="brand">
      <span class="brand-name">BrindleCrewing</span>
      <span class="brand-dot"></span>
    </div>
    <p class="back-url">www.brindlecrewing.com</p>
    <div class="back-band"></div>
  </section>

  <section class="card card-front" aria-label="Business card front">
    <div class="side-stripe">
      <span class="seg-orange"></span>
      <span class="seg-red"></span>
      <span class="seg-yellow"></span>
    </div>

    <div class="brand">
      <span class="brand-name">BrindleCrewing</span>
      <span class="brand-dot"></span>
    </div>

    <div class="person">
      <p class="person-name">Gerald Pinkney</p>
      <p class="person-title">Captain</p>
      <p class="person-address">417 39th Lantern West<br>ALDERMOOR BAY QX 00417</p>
    </div>

    <ul class="contacts">
      <li>
        <svg viewBox="0 0 24 24" aria-hidden="true">
          <circle cx="12" cy="12" r="12" fill="#f04a50"/>
          <path d="M8.2 6.5l2 .2 1 2.6-1.3 1c.7 1.5 1.8 2.6 3.3 3.3l1-1.3 2.6 1 .2 2c-.3.8-1 1.3-1.9 1.2C10.4 16.2 7.8 13.6 7.5 8.9c-.1-.9.4-1.7.7-2.4z" fill="#050505"/>
        </svg>
        555-472-6158
      </li>
      <li>
        <svg viewBox="0 0 24 24" aria-hidden="true">
          <circle cx="12" cy="12" r="12" fill="#f04a50"/>
          <rect x="6" y="8" width="12" height="8.5" rx="1" fill="#050505"/>
          <path d="M6.5 8.5l5.5 4.2 5.5-4.2" stroke="#f04a50" stroke-width="1.2" fill="none"/>
        </svg>
        gpinkney@brindlecrewing.com
      </li>
      <li>
        <svg viewBox="0 0 24 24" aria-hidden="true">
          <circle cx="12" cy="12" r="12" fill="#f04a50"/>
          <g fill="none" stroke="#050505" stroke-width="1.3">
            <circle cx="12" cy="12" r="6"/>
            <ellipse cx="12" cy="12" rx="2.6" ry="6"/>
            <path d="M6 12h12M7 9h10M7 15h10"/>
          </g>
        </svg>
        www.brindlecrewing.com
      </li>
    </ul>
  </section>

</body>
</html>
```